Ridgeford Masonry- Business Card Design

We need a business card design for a new company based in Canberra ACT. We build Rock Retaining Walls, commercial and domestic.
We would like to see designs that use RM letters combine as logo and use stone sandstone or blue rocks. Final design of the business card should communicate strong, wealthy, Rock retaining walls

Target Market(s)

Everybody who needs stone retaining wall in there backyard

Industry/Entity Type

Business

Contact Information for Business Card

RM
Ridgeford Masonry,
Tobin Haraldsen (Stonemason)
Phone/ 0498 315 287
PO Box 3958 Kelvale ACT 2615
E-mail/tharaldsen@oakmail.net.au
www.ridgefordmasonry.com.au

Requirements
Must have
• Letters RM combine as logo. "RIDGEFORD MASONRY" as features
Nice to have
• Rock: Sandstone or bluestone

```html
<!DOCTYPE html>
<html lang="en">
<head>
<meta charset="utf-8">
<title>Ridgeford Masonry – Business Card</title>
<link href="https://fonts.googleapis.com/css2?family=Belleza&display=swap" rel="stylesheet">
<style>
  :root {
    --card-white: #ffffff;
    --ink: #111111;
    --brand-blue: #0a69b3;
    --stone-light: #e2dacb;
    --stone-mid: #cbbfa9;
    --stone-dark: #b3a68e;
  }
  html, body {
    margin: 0;
    padding: 0;
    overflow: hidden;
    background: var(--card-white);
  }
  .card {
    position: relative;
    width: 1200px;
    height: 693px;
    overflow: hidden;
    background: var(--card-white);
    font-family: "Belleza", "Trebuchet MS", sans-serif;
    color: var(--ink);
  }
  .stone-wall {
    position: absolute;
    top: 0;
    left: 0;
    width: 1200px;
    height: 693px;
  }
  .brand-mark {
    position: absolute;
    left: 360px;
    top: 60px;
    width: 172px;
    height: 172px;
    border-radius: 50%;
    background: var(--brand-blue);
  }
  .brand-name {
    position: absolute;
    left: 570px;
    top: 122px;
    margin: 0;
    font-size: 52px;
    font-weight: 400;
    line-height: 60px;
    color: var(--ink);
  }
  .person {
    position: absolute;
    left: 0;
    width: 1200px;
    text-align: center;
    margin: 0;
    font-weight: 400;
  }
  .person-name { top: 286px; font-size: 46px; }
  .person-role { top: 352px; font-size: 33px; }
  .contact {
    position: absolute;
    font-size: 34px;
    line-height: 40px;
    white-space: nowrap;
  }
  .contact-phone { left: 370px; top: 436px; }
  .contact-pobox { left: 668px; top: 436px; }
  .contact-suburb { left: 152px; top: 496px; }
  .contact-email { left: 600px; top: 496px; }
  .icon { position: absolute; }
  .icon-phone { left: 312px; top: 432px; width: 50px; height: 50px; }
  .icon-mail { left: 520px; top: 500px; width: 68px; height: 40px; }
  .web-band {
    position: absolute;
    left: 0;
    top: 565px;
    width: 1200px;
    height: 64px;
    background: var(--brand-blue);
    color: var(--card-white);
    font-size: 47px;
    line-height: 64px;
    text-align: center;
  }
</style>
</head>
<body>
<div class="card">
  <svg class="stone-wall" viewBox="0 0 1200 693" role="img" aria-label="Stacked sandstone wall texture framing the left and right edges of the card">
    <defs>
      <linearGradient id="sandstone" x1="0" y1="0" x2="1" y2="1">
        <stop offset="0" stop-color="var(--stone-light)"/>
        <stop offset="0.55" stop-color="var(--stone-mid)"/>
        <stop offset="1" stop-color="var(--stone-dark)"/>
      </linearGradient>
    </defs>
    <polygon fill="url(#sandstone)" points="0,0 275,0 275,60 255,60 255,170 270,170 270,230 235,230 235,330 215,330 215,400 195,400 195,470 120,470 120,560 140,560 140,640 205,640 205,693 0,693"/>
    <polygon fill="url(#sandstone)" points="1085,0 1200,0 1200,693 995,693 995,640 985,640 985,570 1060,570 1060,480 915,480 915,360 935,360 935,290 895,290 895,180 880,180 880,150 845,150 845,95 1000,95 1000,40 1085,40"/>
  </svg>

  <div class="brand-mark" aria-hidden="true"></div>
  <h1 class="brand-name">Ridgeford<br>Masonry</h1>

  <p class="person person-name">Tobin Haraldsen</p>
  <p class="person person-role">Stonemason</p>

  <svg class="icon icon-phone" viewBox="0 0 50 50" aria-hidden="true">
    <circle cx="25" cy="25" r="22" fill="none" stroke="var(--brand-blue)" stroke-width="3"/>
    <path d="M19 12 q-6 4 -4 14 q3 10 11 13 l4 -5 l-5 -4 l-3 2 q-4 -4 -4 -10 l3 -2 l-1 -7 z" fill="var(--brand-blue)"/>
  </svg>
  <span class="contact contact-phone">0498 315 287</span>
  <span class="contact contact-pobox">PO Box 3958</span>

  <span class="contact contact-suburb">Kelvale ACT 2615</span>
  <svg class="icon icon-mail" viewBox="0 0 68 40" aria-hidden="true">
    <polygon points="4,8 60,2 64,34 8,38" fill="none" stroke="var(--ink)" stroke-width="2"/>
    <polyline points="4,8 36,22 60,2" fill="none" stroke="var(--ink)" stroke-width="2"/>
    <text x="34" y="32" font-size="20" text-anchor="middle" fill="var(--brand-blue)" font-family="Arial, sans-serif">@</text>
  </svg>
  <span class="contact contact-email">tharaldsen@oakmail.net.au</span>

  <div class="web-band">www.ridgefordmasonry.com.au</div>
</div>
</body>
</html>
```